House flipping business web site needed

pinecrestholdingsgroup.com.
I am a residential developer in Northern NJ and I am looking for a fresh new updated website. I have an intro video about my company being made now. I don't update it very often but I want an easy format that I can add update photos to on projects I have worked on or homes I renovate for sale.

Target Market(s)

investors into my projects so a portfolio , people looking to sell their homes to me.

Industry/Entity Type

Real Estate Development

Number of Pages Required

4 page

Font styles to use
Serif

Colors
33b8a4
39a9d7
cadf82

Requirements
Must have
• space for an intro video about my company
• a portfolio with pictures and information about each project
• Markets we serve- Morris County, NJ
• My logo- already created
• SEO
• Yes I would like this to function over all platforms. Phone, computer, all platforms.
• history and background page
• I am looking for a completed page that I can upload to the site that hosts my website
Nice to have
• I want something creative, easy to navigate. modern.

```html
<!DOCTYPE html>
<html lang="en">
<head>
<meta charset="utf-8">
<title>Pinecrest Holdings Group</title>
<link rel="stylesheet" href="https://fonts.googleapis.com/css2?family=Arvo:wght@400;700&family=Open+Sans:ital,wght@0,400;0,600;1,400&display=swap">
<style>
:root{
  --teal:#33b8a4;
  --sky:#39a9d7;
  --lime:#cadf82;
  --ink:#222;
  --body:#555;
  --white:#fff;
  --dark:#1e2a22;
  --line:#e4e4e4;
}
*{margin:0;padding:0;box-sizing:border-box}
html,body{width:1200px;height:3666px;overflow:hidden;background:var(--white)}
body{position:relative;font-family:"Open Sans",sans-serif;color:var(--body)}
.serif{font-family:"Arvo",serif}
.abs{position:absolute}

/* header */
.site-header{position:absolute;left:0;top:0;width:1200px;height:115px;background:var(--white)}
.brand{position:absolute;left:95px;top:14px;width:150px;height:90px;display:flex;align-items:center;gap:8px}
.brand-mark{width:18px;height:18px;border-radius:50%;background:var(--teal);flex:none}
.brand-name{font-family:"Arvo",serif;font-size:17px;line-height:1.15;color:var(--sky);font-weight:700}
.contact-bar{position:absolute;top:26px;right:95px;display:flex;gap:50px;font-size:12px;color:var(--ink)}
.contact-item{display:flex;align-items:center;gap:12px}
.contact-icon{width:30px;height:30px;border-radius:50%;background:var(--teal);display:flex;align-items:center;justify-content:center}
.main-nav{position:absolute;top:80px;left:365px;width:740px;display:flex;justify-content:space-between;font-size:12px;font-weight:600;color:var(--ink);letter-spacing:.5px}

/* hero */
.hero{position:absolute;left:0;top:115px;width:1200px;height:601px;background:linear-gradient(180deg,#5f7a94 0%,#6f7f86 45%,#4d5a4a 78%,#3f6b2c 100%)}
.hero-title{position:absolute;top:240px;width:100%;text-align:center;font-family:"Arvo",serif;font-size:52px;color:var(--white)}
.hero-sub{position:absolute;top:312px;width:100%;text-align:center;font-family:"Arvo",serif;font-size:30px;color:var(--white)}
.btn{display:inline-block;background:var(--teal);color:var(--white);font-family:"Arvo",serif;font-size:15px;text-align:center}
.hero .btn{position:absolute;left:510px;top:375px;width:180px;height:46px;line-height:46px}

/* welcome */
.section-kicker{position:absolute;width:100%;text-align:center;font-family:"Arvo",serif;font-size:30px;color:var(--ink)}
.section-title{position:absolute;width:100%;text-align:center;font-family:"Arvo",serif;font-size:36px;color:var(--ink);letter-spacing:1px}
.lead{position:absolute;left:160px;width:880px;text-align:center;font-size:12.5px;line-height:24px;color:var(--body)}

/* video */
.video{position:absolute;left:0;top:1090px;width:1200px;height:491px;background:linear-gradient(180deg,#2f3a22 0%,#4a4f3c 40%,#3e4b2c 75%,#3b6a25 100%)}
.video-title{position:absolute;top:283px;width:100%;text-align:center;font-family:"Arvo",serif;font-size:34px;color:var(--white);letter-spacing:1px}

/* markets */
.markets-photo{position:absolute;left:0;top:1581px;width:600px;height:465px;background:linear-gradient(160deg,#8fa38a 0%,#c7b79e 50%,#b55a3e 100%)}
.markets{position:absolute;left:600px;top:1581px;width:600px;height:465px;background:var(--teal);color:var(--white)}
.markets h2{position:absolute;left:98px;top:92px;font-family:"Arvo",serif;font-weight:400;font-size:34px;letter-spacing:1px}
.markets h3{position:absolute;left:98px;top:137px;font-family:"Arvo",serif;font-weight:400;font-size:28px;letter-spacing:1px}
.markets p{position:absolute;left:98px;top:186px;width:420px;font-size:13px;line-height:24px}
.btn-outline{position:absolute;left:104px;top:332px;width:150px;height:44px;line-height:42px;border:1.5px solid var(--white);text-align:center;font-family:"Arvo",serif;font-size:14px}

/* portfolio */
.portfolio-grid{position:absolute;left:98px;top:2366px;width:1004px;display:grid;grid-template-columns:repeat(4,243px);grid-auto-rows:189px;gap:9px 11px}
.project-photo{display:block}
.portfolio .btn{position:absolute;left:526px;top:2797px;width:148px;height:44px;line-height:44px}

/* testimonials */
.testimonials{position:absolute;left:0;top:2913px;width:1200px;height:455px;background:linear-gradient(180deg,#15201a 0%,#2a3329 55%,#3a3d33 100%)}
.testimonials h2{position:absolute;top:90px;width:100%;text-align:center;font-family:"Arvo",serif;font-weight:400;font-size:34px;color:var(--white);letter-spacing:1px}
.client-photo{position:absolute;left:262px;top:172px;width:184px;height:184px;border-radius:50%;border:4px solid var(--white);background:radial-gradient(circle at 50% 40%,#c99c7f,#5f7d9a)}
.quote{position:absolute;left:520px;top:193px;width:400px;font-size:12.5px;line-height:24px;font-style:italic;color:var(--white)}
.client-name{position:absolute;left:522px;top:325px;font-family:"Arvo",serif;font-size:15px;color:var(--white)}
.client-role{position:absolute;left:522px;top:349px;font-size:11px;color:#ddd}

/* footer */
.site-footer{position:absolute;left:0;top:3368px;width:1200px;height:298px;background:var(--white)}
.footer-brand{position:absolute;left:83px;top:14px;width:208px;height:190px;background:#f4f4f4;display:flex;align-items:center;justify-content:center;gap:8px;padding:0 14px}
.footer-col{position:absolute;top:54px}
.footer-col h4{font-family:"Arvo",serif;font-weight:400;font-size:16px;color:var(--ink);margin-bottom:14px}
.footer-col li{list-style:none;font-size:11.5px;line-height:21px;color:var(--ink)}
.footer-col .highlight{color:var(--sky);font-size:12.5px}
.social{display:flex;gap:8px;margin-top:14px}
.social span{width:33px;height:33px;border-radius:50%}
.copyright{position:absolute;top:3614px;width:100%;text-align:center;font-size:11px;color:var(--ink)}
</style>
</head>
<body>

<header class="site-header">
  <div class="brand"><span class="brand-mark"></span><span class="brand-name">Pinecrest Holdings Group</span></div>
  <div class="contact-bar">
    <div class="contact-item">
      <span class="contact-icon"><svg width="14" height="14" viewBox="0 0 24 24"><path fill="#fff" d="M6.6 10.8a15 15 0 0 0 6.6 6.6l2.2-2.2c.3-.3.7-.4 1-.2 1.1.4 2.3.6 3.6.6.6 0 1 .4 1 1V20c0 .6-.4 1-1 1A17 17 0 0 1 3 4c0-.6.4-1 1-1h3.5c.6 0 1 .4 1 1 0 1.2.2 2.4.6 3.6.1.3 0 .7-.2 1z"/></svg></span>
      <span>CALL US : (555) 365 0142</span>
    </div>
    <div class="contact-item">
      <span class="contact-icon"><svg width="14" height="12" viewBox="0 0 24 18"><rect x="1" y="1" width="22" height="16" rx="2" fill="#fff"/><path d="M2 2l10 8 10-8" stroke="#33b8a4" stroke-width="2" fill="none"/></svg></span>
      <span>EMAIL US : info@pinecrestholdingsgroup.com</span>
    </div>
  </div>
  <nav class="main-nav">
    <span>HOME</span><span>ABOUT</span><span>CONTACT</span><span>PORTFOLIO</span><span>VIDEOS</span><span>BLOG</span><span>TESTIMONIALS</span>
  </nav>
</header>

<section class="hero" role="img" aria-label="Photo of a large renovated stone and shingle house with a front lawn">
  <h1 class="hero-title">Pinecrest Holdings Group</h1>
  <p class="hero-sub">Investing in our neighborhoods</p>
  <span class="btn">CONTACT HERE!</span>
</section>

<section class="welcome">
  <p class="section-kicker" style="top:795px">WELCOME TO</p>
  <h2 class="section-title" style="top:838px;font-weight:400">PINECREST HOLDINGS GROUP</h2>
  <p class="lead" style="top:910px">We are a team of experienced home buyers and renovators in the Morris County, NJ area. Our specialty is purchasing distressed homes and property. We then collaborate with the best talents in Northern New Jersey to renovate those properties and transform them into the best house in the neighborhood. As a result we create equity, a return on investment and most importantly we give home buyers a worry free property that provides a better way of life and hope for their future.</p>
</section>

<section class="video" role="img" aria-label="Video still of an old shed-style house among trees, intro video about the company">
  <svg class="abs" style="left:554px;top:160px" width="92" height="92" viewBox="0 0 92 92"><circle cx="46" cy="46" r="43" fill="none" stroke="#fff" stroke-width="4"/><path d="M36 28l30 18-30 18z" fill="#fff"/></svg>
  <h2 class="video-title" style="font-weight:400">ABOUT MY COMPANY</h2>
</section>

<div class="markets-photo" role="img" aria-label="Photo of a smiling family in front of their home"></div>
<section class="markets">
  <h2>MARKETS WE SERVE</h2>
  <h3>MORRIS COUNTY, NJ</h3>
  <p>We are a team of experienced home buyers and renovators in the Morris County, NJ area. Our specialty is purchasing distressed homes and property. We then collaborate with the best talents in Northern New Jersey to renovate those properties and transform them into the best house in the neighborhood...</p>
  <span class="btn-outline">CLICK HERE</span>
</section>

<section class="portfolio">
  <p class="section-kicker" style="top:2125px">PORTFOLIO</p>
  <h2 class="section-title" style="top:2166px;font-weight:400">PINECREST HOLDINGS GROUP</h2>
  <p class="lead" style="top:2228px;left:140px;width:920px">Many upgrades to this home. Added a new full bath, family room, office, kitchenette and kids play room in walk out basement with 2 triple french doors. New 1/2 bath was added off of the dining room with large walk in storage closet off main living area. Washer and dryer were re-located to second floor. Radiant heat installed in basement and first floor bathroom, office and walk in closet. New stone facade to front of home. Rock walls and landscaping including fence around the yard.</p>
  <div class="portfolio-grid">
    <span class="project-photo" role="img" aria-label="Project photo: renovated two-story house exterior" style="background:linear-gradient(180deg,#cfd6dd,#a59b86 60%,#5e6a3e)"></span>
    <span class="project-photo" role="img" aria-label="Project photo: house during renovation" style="background:linear-gradient(180deg,#c7ccd0,#8d8a78 60%,#6a604e)"></span>
    <span class="project-photo" role="img" aria-label="Project photo: dark green sided house" style="background:linear-gradient(180deg,#6fb6e0,#3c5a60 55%,#2e3d3a)"></span>
    <span class="project-photo" role="img" aria-label="Project photo: house with stone retaining wall" style="background:linear-gradient(180deg,#8cc4ea,#dfe2e2 50%,#8e7a60)"></span>
    <span class="project-photo" role="img" aria-label="Project photo: front of restored house with rock walls" style="background:linear-gradient(180deg,#c9d3dc,#b9aa8c 55%,#5b5644)"></span>
    <span class="project-photo" role="img" aria-label="Project photo: new rear deck and porch" style="background:linear-gradient(180deg,#9fb8d3,#7d6c5e 60%,#4d4a48)"></span>
    <span class="project-photo" role="img" aria-label="Project photo: finished basement family room" style="background:linear-gradient(180deg,#3a2f28,#6e5a48 55%,#2d2622)"></span>
    <span class="project-photo" role="img" aria-label="Project photo: radiant heat tubing on floor" style="background:linear-gradient(160deg,#8a3b52,#3e5a9a 55%,#b04a5c)"></span>
  </div>
  <span class="btn">VIEW MORE</span>
</section>

<section class="testimonials" role="img" aria-label="Dark photo of a house at dusk behind the client quote">
  <h2>WHAT OUR CLIENT'S SAY</h2>
  <div class="client-photo" role="img" aria-label="Portrait of the client"></div>
  <p class="quote">Lorem Ipsum is simply dummy text of the printing and typesetting industry. Lorem Ipsum has been the industry's standard dummy text ever since the 1500s, when an unknown printer took a galley of type and scrambled it to make a type specimen book.</p>
  <p class="client-name">Marcus Bell</p>
  <p class="client-role">Business man</p>
</section>

<footer class="site-footer">
  <div class="footer-brand"><span class="brand-mark"></span><span class="brand-name">Pinecrest Holdings Group</span></div>
  <div class="footer-col" style="left:350px">
    <h4>Welcome</h4>
    <ul><li>Home</li><li>About</li><li>Contact</li><li>Portfolio</li><li>Videos</li></ul>
  </div>
  <div class="footer-col" style="left:498px">
    <h4>Information</h4>
    <ul><li>Terms &amp; Conditions</li><li>Privacy Policy</li><li>Disclaimer</li><li>Sitemap</li></ul>
  </div>
  <div class="footer-col" style="left:668px">
    <h4>Contact info</h4>
    <ul><li class="highlight">Pinecrest Holdings Group</li><li>Morris County, NJ</li><li>862-555-0148</li><li>Phone: (555) 365 0142</li><li>E-mail: info@pinecrestholdingsgroup.com</li></ul>
  </div>
  <div class="footer-col" style="left:904px">
    <h4>Follow us</h4>
    <ul><li>Connect with our social network</li></ul>
    <div class="social">
      <span style="background:#3b5a98"></span><span style="background:#1d75b3"></span><span style="background:#f39a1e"></span><span style="background:var(--sky)"></span><span style="background:#d8312a"></span>
    </div>
  </div>
</footer>
<p class="copyright">© 2016, Pinecrest Holdings Group. All Rights Reserved</p>

</body>
</html>
```